Bref créative
Harbor Floors & More --- Business card
Harbor Floors & More - thousands of types of tiles
Simple
Mei Dalton
4150 Marwood Ave,
Unit 3B, Concord, ON
L4K 5R8
mei.dalton@harborfloorsmore.example
www.harborfloorsmore.example
Introduction : Harbor Floors & More imports and distributes thousands of types of tiles in limestone, marble, slate, granite, porcelan, ceramic, glass and aluminum for homeowners, builders and contractors. Also providing custom-made solid wood kitchen cabinet and vanities.
the logo of Harbor Floors & More
Logo on Black
Logo on White

```html
<!DOCTYPE html>
<html lang="en">
<head>
<meta charset="utf-8">
<title>Harbor Floors &amp; More — Business Card</title>
<link rel="stylesheet" href="https://fonts.googleapis.com/css2?family=Open+Sans:wght@400;600&display=swap">
<style>
  :root {
    --page-bg: #eceeea;
    --card-white: #ffffff;
    --lime-light: #c4dc3c;
    --lime: #9cc41c;
    --lime-deep: #7fa512;
    --swoosh-blue: #1fa0dc;
    --swoosh-pale: #bfe3f3;
    --ink-teal: #1f5d6e;
    --text-light: #ffffff;
  }
  * { box-sizing: border-box; margin: 0; padding: 0; }
  html, body {
    width: 1200px; height: 1065px; overflow: hidden;
    background: var(--page-bg);
    font-family: "Open Sans", Arial, sans-serif;
  }
  .sheet {
    width: 1200px; height: 1065px;
    display: flex; flex-direction: column; align-items: center; justify-content: center;
    gap: 44px;
  }
  .card {
    position: relative;
    width: 820px; height: 469px;
    border-radius: 28px;
    overflow: hidden;
    box-shadow: 0 10px 28px rgba(0,0,0,0.18);
  }
  /* Front */
  .card-front { background: var(--card-white); }
  .card-front .wave { position: absolute; inset: 0; width: 100%; height: 100%; }
  .brand {
    position: absolute; top: 118px; left: 0; right: 0;
    display: flex; align-items: center; justify-content: center; gap: 16px;
  }
  .brand-dot {
    width: 26px; height: 26px; border-radius: 50%;
    background: var(--swoosh-blue);
  }
  .brand-name {
    font-family: "Open Sans", Arial, sans-serif;
    font-weight: 600;
    font-size: 36px; color: var(--ink-teal);
  }
  .contact {
    position: absolute; bottom: 52px;
    color: var(--text-light); font-size: 15px; line-height: 1.6;
    font-style: normal;
  }
  .contact-address { left: 70px; }
  .contact-person { left: 440px; }
  .person-name { font-weight: 600; font-size: 18px; margin-bottom: 4px; }
  .contact-line { display: flex; align-items: center; gap: 8px; }
  .contact-line svg { width: 14px; height: 14px; flex: none; }
  /* Back */
  .card-back {
    background: radial-gradient(ellipse at 45% 30%, var(--lime-light) 0%, var(--lime) 55%, var(--lime-deep) 100%);
  }
  .back-url {
    position: absolute; right: 60px; bottom: 70px;
    color: var(--text-light); font-size: 20px; letter-spacing: 3px;
  }
</style>
</head>
<body>
<main class="sheet">
  <section class="card card-front" aria-label="Business card front">
    <svg class="wave" viewBox="0 0 820 469" preserveAspectRatio="none" aria-hidden="true">
      <defs>
        <linearGradient id="limeFill" x1="0" y1="0" x2="0" y2="1">
          <stop offset="0" stop-color="#c4dc3c"/>
          <stop offset="1" stop-color="#8cb617"/>
        </linearGradient>
      </defs>
      <path d="M0 250 C220 190 420 330 820 260 L820 469 L0 469 Z" fill="url(#limeFill)"/>
      <path d="M0 232 C230 170 430 305 820 240" fill="none" stroke="#bfe3f3" stroke-width="10"/>
      <path d="M0 242 C230 182 430 318 820 250" fill="none" stroke="#1fa0dc" stroke-width="6"/>
    </svg>
    <div class="brand">
      <span class="brand-dot" aria-hidden="true"></span>
      <span class="brand-name">Harbor Floors &amp; More</span>
    </div>
    <address class="contact contact-address">
      4150 Marwood Ave,<br>
      Unit 3B, Concord, ON<br>
      L4K 5R8
    </address>
    <div class="contact contact-person">
      <p class="person-name">Mei Dalton</p>
      <p class="contact-line">
        <svg viewBox="0 0 24 24" aria-hidden="true"><path fill="#fff" d="M6.6 10.8a15 15 0 0 0 6.6 6.6l2.2-2.2a1 1 0 0 1 1-.25 11.4 11.4 0 0 0 3.6.57 1 1 0 0 1 1 1V20a1 1 0 0 1-1 1A17 17 0 0 1 3 4a1 1 0 0 1 1-1h3.5a1 1 0 0 1 1 1c0 1.25.2 2.45.57 3.6a1 1 0 0 1-.25 1z"/></svg>
        416 555 0142
      </p>
      <p class="contact-line">
        <svg viewBox="0 0 24 24" aria-hidden="true"><path fill="#fff" d="M3 5h18v14H3z M4 6l8 6 8-6" stroke="#9cc41c" stroke-width="1.5"/></svg>
        mei.dalton@harborfloorsmore.example
      </p>
      <p class="contact-line">
        <svg viewBox="0 0 24 24" aria-hidden="true"><circle cx="12" cy="12" r="9" fill="none" stroke="#fff" stroke-width="2"/><path d="M3 12h18M12 3c3 3 3 15 0 18M12 3c-3 3-3 15 0 18" fill="none" stroke="#fff" stroke-width="1.5"/></svg>
        www.harborfloorsmore.example
      </p>
    </div>
  </section>

  <section class="card card-back" aria-label="Business card back">
    <p class="back-url">www.harborfloorsmore.example</p>
  </section>
</main>
</body>
</html>
```